Existing Cardiology Practice now offering New PET MPI Services Brochure

We are a private group cardiology practice that is opening a new PET MPI services. We would like a brochure that emphasizes our New PET MPI and what that is as well as all of our other services offered at our practice. Minimally The front of the brochure should have the physician group picture with their names, our clinic logo, the PET MPI, our address, phone, fax, website. The inside should include the information regarding what the PET MPI is (included as an attachment to this project). The back should have the map with our location on it, and all the other services offered as written on the attachment to this project. When listing the services on the back , please make sure you spell everything correctly and list them accordingly. The names of the physicians in order from Left to Right are Korvan Dilesh, MD, Marvetto Quilanshu, MD, Tovrin Gulak, MD, Pelvor Gulak, MD. The brochure should be 8 1/2 inches in height and when opened be 11 inches in length. It will be a bifold brochure.

Target Market(s)

Healthcare Providers, healthcare facilities, patients.

Industry/Entity Type

Health Care

Font styles to use
Sans Serif

Requirements
Must have
• Physician Group Picture, Logo, New PET MPI, address, phone 555-214-7318, Fax 555-214-7319. Web address www.quenmorecardio.example. Services Offered listing, PET MPI information, Map Picture.
Nice to have
• Open to suggestions
Should not have
• Not sure

```html
<!DOCTYPE html>
<html lang="en">
<head>
<meta charset="utf-8">
<title>Quenmore Cardio – The PET MPI Brochure</title>
<link href="https://fonts.googleapis.com/css2?family=Montserrat:wght@500;600;700;800&family=Open+Sans:wght@400;600&family=Lora:ital@1&display=swap" rel="stylesheet">
<style>
:root{
  --slate:#4b6581;
  --slate-dark:#3e566f;
  --red:#c8313f;
  --ink:#2b2b2b;
  --muted:#555b61;
  --paper:#ffffff;
  --paper-grey:#f1f2f3;
  --stage:#e7e4e0;
}
*{box-sizing:border-box;margin:0;padding:0}
html,body{width:1200px;height:900px;overflow:hidden;background:var(--stage)}
body{font-family:"Open Sans",Arial,sans-serif;color:var(--ink);display:flex;align-items:center;justify-content:center;gap:18px}
.spread{width:582px;height:450px;display:flex;box-shadow:0 6px 18px rgba(0,0,0,.18);background:var(--paper)}
.panel{width:50%;height:100%;position:relative;overflow:hidden}
h2,h3,.display{font-family:"Montserrat",Arial,sans-serif}

/* ===== Back panel ===== */
.back{background:var(--slate);color:#fff;padding:22px 16px 14px}
.back h2{font-size:10.5px;font-weight:800;letter-spacing:.2px;margin-bottom:8px}
.hosp-list{display:grid;grid-template-columns:1fr 1fr;gap:6px 10px;margin-bottom:12px}
.svc{display:flex;align-items:center;gap:6px;font-size:5.6px;line-height:1.35}
.svc .ring{flex:0 0 17px;height:17px;border:1px solid #fff;border-radius:50%;display:flex;align-items:center;justify-content:center}
.svc .ring i{width:7px;height:7px;border:1px solid #fff;border-radius:2px}
.office{display:grid;grid-template-columns:1.15fr 1fr;gap:8px;margin-bottom:8px}
.office h4{font-family:"Montserrat",sans-serif;font-size:6px;font-weight:700;margin-bottom:2px}
.office ul,.lab-list{list-style:none;font-size:5.2px;line-height:1.45}
.office li::before,.lab-list li::before{content:"• "}
.lab-list{font-family:"Montserrat",sans-serif;font-weight:600;font-size:5.6px;margin-bottom:10px}
.back-foot{display:flex;gap:10px;align-items:flex-start}
.brand-block{flex:1 1 auto;min-width:0}
.brand-block .brand{font-family:"Montserrat",sans-serif;font-weight:800;font-size:9px;white-space:nowrap}
.brand-block .tag{font-size:6px;line-height:1.3;margin-bottom:10px}
.brand-block h3{font-size:8.5px;font-weight:800;margin-bottom:5px}
.contact{list-style:none;font-size:6.4px;display:grid;gap:4px}
.contact li{display:flex;align-items:center;gap:5px;white-space:nowrap}
.map-block{flex:0 0 132px}
.map{width:132px;height:86px;background:linear-gradient(135deg,#eeeeee,#f6dede 60%,#e9ece9);border:2px solid #fff}
.back-addr{font-size:6.2px;margin-top:6px;text-align:right;white-space:nowrap}
.icon{width:8px;height:8px;flex:0 0 8px}

/* ===== Front panel ===== */
.front{background:var(--slate)}
.cover-photo{position:absolute;inset:0 0 38% 0;background:linear-gradient(160deg,#eef0f2 0%,#d5dbe1 45%,#e58a8f 62%,#c9d2da 80%)}
.logo{position:absolute;top:16px;left:0;right:0;display:flex;align-items:center;justify-content:center;gap:5px}
.logo .dot{width:9px;height:9px;border-radius:50%;background:var(--red)}
.logo .name{font-family:"Montserrat",sans-serif;font-weight:800;font-size:14px;color:var(--red);letter-spacing:.5px}
.logo-tag{position:absolute;top:36px;left:0;right:0;text-align:center;font-size:5.5px;color:var(--red)}
.docs{position:absolute;top:218px;left:12px;right:12px;display:flex;justify-content:space-between}
.doc{width:58px;text-align:center;color:#fff}
.doc .photo{height:62px;background:linear-gradient(180deg,#7d8a96,#3d4b58);border:2px solid #fff;margin-bottom:4px}
.doc .nm{font-family:"Montserrat",sans-serif;font-weight:700;font-size:5.6px;line-height:1.25}
.doc .cred{font-size:5px}
.front .title{position:absolute;top:318px;left:0;right:0;text-align:center;font-size:24px;font-weight:800;color:#fff;letter-spacing:.5px}
.front-contact{position:absolute;top:364px;left:14px;right:14px;display:flex;justify-content:space-between;color:#fff;font-size:7px}
.front-contact span{display:flex;align-items:center;gap:4px;white-space:nowrap}
.front-addr{position:absolute;top:392px;left:0;right:0;text-align:center;color:#fff;font-size:8px}

/* ===== Inside ===== */
.inside-left{background:var(--paper-grey)}
.ph{position:absolute}
.ph-stetho{top:0;left:0;right:0;height:140px;background:linear-gradient(135deg,#f7f7f7,#dcdcdc 55%,#e7b3b6)}
.benefit-h{position:absolute;top:150px;left:16px;right:16px;font-family:"Montserrat",sans-serif;font-weight:800;font-size:9.5px;color:var(--red)}
.benefit-p{position:absolute;top:164px;left:16px;right:16px;font-size:5.6px;color:var(--muted)}
.ph-lab{top:182px;left:0;width:140px;height:110px;background:linear-gradient(135deg,#dfe8f1,#b9cadb)}
.red-box{position:absolute;top:182px;left:150px;right:12px;background:var(--red);color:#fff;padding:8px 8px;list-style:none;font-size:5.4px;line-height:1.55}
.red-box li::before{content:"• "}
.copy{position:absolute;left:16px;right:16px;font-size:5.2px;line-height:1.5;color:var(--muted)}
.copy h3{font-size:9px;font-weight:800;color:var(--red);margin-bottom:2px}
.safety{top:300px}
.about{top:340px}
.band{position:absolute;left:0;right:0;bottom:0;height:22px;background:var(--red);color:#fff;display:flex;align-items:center;justify-content:space-around;font-size:6.6px}
.band span{display:flex;align-items:center;gap:4px;white-space:nowrap}
.inside-right{background:var(--paper)}
.expect{position:absolute;top:18px;left:16px;right:14px}
.expect-head{display:flex;align-items:center;justify-content:space-between;border-top:1px solid var(--red);padding-top:5px;margin-bottom:5px}
.expect-head h3{font-size:9.5px;font-weight:800;color:var(--red)}
.mini-logo{font-family:"Montserrat",sans-serif;font-weight:800;font-size:5.5px;color:var(--red)}
.expect p{font-size:5.2px;line-height:1.5;color:var(--ink);margin-bottom:5px}
.expect .lead{font-family:"Lora",Georgia,serif;font-style:italic;font-size:7.5px;color:var(--red)}
.ph-couple{left:0;right:0;top:268px;bottom:22px;background:linear-gradient(180deg,#cfe0ee 0%,#a9c3d8 40%,#8ea57c 75%,#9c9a92)}
</style>
</head>
<body>

<svg width="0" height="0" style="position:absolute">
  <defs>
    <symbol id="i-phone" viewBox="0 0 16 16"><circle cx="8" cy="8" r="7.2" fill="none" stroke="currentColor" stroke-width="1.2"/><path d="M5.5 4.5l1.5 0 .7 2-1 .8a5 5 0 0 0 2 2l.8-1 2 .7v1.5c-3.5.3-6.3-2.5-6-6z" fill="currentColor"/></symbol>
    <symbol id="i-fax" viewBox="0 0 16 16"><circle cx="8" cy="8" r="7.2" fill="none" stroke="currentColor" stroke-width="1.2"/><rect x="4.5" y="6.5" width="7" height="4.5" fill="currentColor"/><rect x="6" y="4" width="4" height="2.5" fill="none" stroke="currentColor"/></symbol>
    <symbol id="i-web" viewBox="0 0 16 16"><circle cx="8" cy="8" r="7.2" fill="none" stroke="currentColor" stroke-width="1.2"/><circle cx="8" cy="8" r="4" fill="none" stroke="currentColor"/><path d="M4 8h8M8 4v8" stroke="currentColor"/></symbol>
  </defs>
</svg>

<!-- Outside: back + front cover -->
<section class="spread outside">
  <div class="panel back">
    <h2>HOSPITAL SERVICES PROVIDED</h2>
    <div class="hosp-list">
      <div class="svc"><span class="ring"><i></i></span>Trans Radial Cardiac and Peripheral Procedures</div>
      <div class="svc"><span class="ring"><i></i></span>Transcatheter Leaflet Clip Procedure for Mitral Regurgitation</div>
      <div class="svc"><span class="ring"><i></i></span>Angioplasty &amp; Stent Implantation for Heart, Kidney, Extremities &amp; Carotid Circulation Disorders</div>
      <div class="svc"><span class="ring"><i></i></span>ASD/PFO Closure</div>
      <div class="svc"><span class="ring"><i></i></span>Left Atrial Appendage Closure for Patients with Atrial Fibrillation</div>
      <div class="svc"><span class="ring"><i></i></span>Left Ventricular Assist Support for Complex Interventions</div>
      <div class="svc"><span class="ring"><i></i></span>Trans-Catheter Aortic Valve Replacement (TAVR)</div>
      <div class="svc"><span class="ring"><i></i></span>Catheter Directed Therapies for Pulmonary Embolism</div>
    </div>
    <h2>OFFICE SERVICES PROVIDED</h2>
    <div class="office">
      <div>
        <h4>Consultation and Preventive Screening for:</h4>
        <ul>
          <li>Coronary Artery Disease</li>
          <li>Peripheral Arterial/Venous Disease/Carotid Artery Disease</li>
          <li>Lipid and Blood Pressure &amp; Blood Sugar Disorders</li>
          <li>Advanced Heart Failure and Valvular Heart Disease</li>
        </ul>
      </div>
      <div>
        <h4>Cardiac and Vascular Ultrasound<br>Nuclear Stress Imaging<br>Arrhythmia Evaluation:</h4>
        <ul>
          <li>EKG, Holter, and Event Monitor</li>
          <li>Implantable Loop Monitor</li>
        </ul>
      </div>
    </div>
    <ul class="lab-list">
      <li>Lab Testing on Site</li>
      <li>External Counter Pulsation Therapy for Advanced Heart Failure &amp; CAD Patients (ECP)</li>
      <li>Screening for Endothelial Dysfunction &amp; Autonomic Dysfunction</li>
      <li>Venous Ablation Therapy</li>
      <li>Cardiac PET MPI</li>
    </ul>
    <div class="back-foot">
      <div class="brand-block">
        <div class="brand">QUENMORE CARDIO</div>
        <div class="tag">CARDIOVASCULAR Center<br>of EXCELLENCE</div>
        <h3>CONTACT US</h3>
        <ul class="contact">
          <li><svg class="icon"><use href="#i-phone"/></svg>555-214-7318</li>
          <li><svg class="icon"><use href="#i-fax"/></svg>555-214-7319</li>
          <li><svg class="icon"><use href="#i-web"/></svg>www.quenmorecardio.example</li>
        </ul>
      </div>
      <div class="map-block">
        <div class="map" role="img" aria-label="Street map marking the clinic location"></div>
        <div class="back-addr">218 Larkfield Road, Suite D, Westmere, TX</div>
      </div>
    </div>
  </div>

  <div class="panel front">
    <div class="cover-photo" role="img" aria-label="Doctor in a white coat holding a red heart with a heartbeat line"></div>
    <div class="logo"><span class="dot"></span><span class="name">QUENMORE CARDIO</span></div>
    <div class="logo-tag">Cardiovascular Center of Excellence</div>
    <div class="docs">
      <div class="doc"><div class="photo" role="img" aria-label="Portrait of Dr. Korvan Dilesh"></div><div class="nm">KORVAN DILESH</div><div class="cred">(MD FACC)</div></div>
      <div class="doc"><div class="photo" role="img" aria-label="Portrait of Dr. Marvetto Quilanshu"></div><div class="nm">MARVETTO QUILANSHU</div><div class="cred">(MD)</div></div>
      <div class="doc"><div class="photo" role="img" aria-label="Portrait of Dr. Tovrin Gulak"></div><div class="nm">TOVRIN GULAK</div><div class="cred">(MD)</div></div>
      <div class="doc"><div class="photo" role="img" aria-label="Portrait of Dr. Pelvor Gulak"></div><div class="nm">PELVOR GULAK</div><div class="cred">(MD)</div></div>
    </div>
    <div class="title display">THE PET MPI</div>
    <div class="front-contact">
      <span><svg class="icon"><use href="#i-phone"/></svg>555-214-7318</span>
      <span><svg class="icon"><use href="#i-fax"/></svg>555-214-7319</span>
      <span><svg class="icon"><use href="#i-web"/></svg>www.quenmorecardio.example</span>
    </div>
    <div class="front-addr">218 Larkfield Road, Suite D, Westmere, TX</div>
  </div>
</section>

<!-- Inside spread -->
<section class="spread inside">
  <div class="panel inside-left">
    <div class="ph ph-stetho" role="img" aria-label="Stethoscope and small red heart beside a keyboard"></div>
    <h3 class="benefit-h">WHO BENEFITS FROM A PET MPI?</h3>
    <p class="benefit-p">Patients benefit from a cardiac PET MPI exam for a variety of reasons, some of them are:</p>
    <div class="ph ph-lab" role="img" aria-label="Lab technician working at a microscope"></div>
    <ul class="red-box">
      <li>Breast implants, large chest</li>
      <li>High-risk patients</li>
      <li>Known or suspected coronary artery disease</li>
      <li>Large body habitus, high BMI</li>
      <li>Prior poor-quality stress imaging study</li>
      <li>Requires pharmacologic stress imaging</li>
      <li>Time-sensitive, emergent</li>
      <li>Unable to exercise</li>
      <li>Young patients with coronary artery disease</li>
      <li>The need for a more accurate test</li>
    </ul>
    <div class="copy safety">
      <h3>SAFETY</h3>
      Cardiac PET MPI scans are a safe and effective diagnostic imaging test. The tracer used is not a dye or contrast and results in minimal radiation exposure and enables a far briefer test.
    </div>
    <div class="copy about">
      <h3>ABOUT US</h3>
      At Quenmore Cardio we strive to provide the highest level and quality of cardiac care available. This requires two commitments. The first commitment is treat the patient as an individual, and the second is to strive for continuous improvement in the technical delivery of care in this increasingly complex field.<br>Quenmore Cardio is a team whose goal is the preservation of good health.
    </div>
    <div class="band">
      <span><svg class="icon"><use href="#i-phone"/></svg>555-214-7318</span>
      <span><svg class="icon"><use href="#i-fax"/></svg>555-214-7319</span>
      <span><svg class="icon"><use href="#i-web"/></svg>www.quenmorecardio.example</span>
    </div>
  </div>

  <div class="panel inside-right">
    <div class="expect">
      <div class="expect-head"><h3>WHAT TO EXPECT</h3><span class="mini-logo">QUENMORE CARDIO</span></div>
      <p>Most cardiac PET exams take less than one hour; however, a longer exam should not be cause for concern. Upon arrival, our team will register you and review your medical history. Please be sure to report all medications you are taking.</p>
      <p class="lead">Trained medical personnel will be with you throughout your exam.</p>
      <p>An intravenous line will be placed in a vein in your arm to allow the administration of medication during the exam. Small pads called electrodes will be placed on your chest to monitor the electrical activity of your heart throughout the study. Your blood pressure, heart rate, and electrocardiogram are monitored before, during, and after the test.</p>
      <p>You will be asked to lie down on a padded, comfortable scanning table developed especially for the PET camera. During your PET scan, the majority of your body is outside the scanner; this is not a full-body scan. If you're claustrophobic, please take your medication 30 minutes before your scan.</p>
      <p>A small amount of radiopharmaceutical is given through your intravenous line, enabling the PET camera to capture images of your heart. The camera will take pictures of your heart in two phases, a resting and stress phase.</p>
      <p>The resting and stress phases are compared to evaluate blood flow through your heart and to look for heart disease and damage to the heart muscle.</p>
      <p>In most cases, you may leave as soon as your cardiac PET MPI study is complete. You will be able to eat, drink, and return to your normal daily activities.</p>
    </div>
    <div class="ph ph-couple" role="img" aria-label="Cheerful older couple sitting outdoors above a river town"></div>
    <div class="band">
      <span><svg class="icon"><use href="#i-phone"/></svg>555-214-7318</span>
      <span><svg class="icon"><use href="#i-fax"/></svg>555-214-7319</span>
      <span><svg class="icon"><use href="#i-web"/></svg>www.quenmorecardio.example</span>
    </div>
  </div>
</section>

</body>
</html>
```